Post Card (5x7) - Pre-foreclosure Image - Harbor Path Partners

(Two-Sided Post Card)
FACING FORECLOSURE? YOU STILL HAVE OPTIONS.
If you’re behind on payments or at risk of foreclosure, you’re not alone—and it’s not too late to take action.
We help homeowners:
• Explore options to stay in their home
• Stop or delay foreclosure
• Sell quickly for a fair price if needed
No pressure. No obligation. Just real solutions tailored to your situation.
Call - (240) 558-2094
Email - marcus@hpbllc-mail.com
Harbor Path Partners LLC
7200 Bramwick Lane, Ellicott City, MD 21043
**Marcus Fennimore is a Licensed Realtor with Copperleaf Homes Realty in Bethesda, Maryland.
(Leave room for mailing address, return address & postage)
Target Market(s)
Distressed Homeowners
Industry/Entity Type
Real Estate

```html
<!DOCTYPE html>
<html lang="en">
<head>
<meta charset="utf-8">
<title>Harbor Path Partners – Pre-foreclosure Postcard</title>
<link href="https://fonts.googleapis.com/css2?family=Anton&family=Bebas+Neue&family=Outfit:wght@500;600;700&display=swap" rel="stylesheet">
<style>
  :root {
    --stage: #a9a9a9;
    --ink: #000000;
    --paper: #ffffff;
    --mist: #f0f0f0;
    --gold: #f7b32b;
    --text-dark: #111111;
  }
  * { margin: 0; padding: 0; box-sizing: border-box; }
  html, body { width: 1200px; height: 969px; overflow: hidden; background: var(--stage); }
  .canvas { position: relative; width: 1200px; height: 969px; }

  .card { position: absolute; top: 169px; width: 451px; height: 631px; overflow: hidden; }
  .card--front { left: 138px; background: var(--ink); }
  .card--back { left: 611px; background: var(--paper); }
  .card svg.shapes { position: absolute; inset: 0; width: 100%; height: 100%; }

  /* Front */
  .front-photo {
    position: absolute; left: 0; top: 0; width: 451px; height: 360px;
    background: linear-gradient(180deg, #8a7a66 0%, #b78a52 45%, #6a4a2a 75%, #3a2818 100%);
  }
  .brand-tag {
    position: absolute; left: 267px; top: 50px; width: 184px;
    text-align: center; font-family: 'Outfit', sans-serif; font-weight: 600;
    color: var(--text-dark); font-size: 15px; line-height: 18px; letter-spacing: 2px;
  }
  .front-headline {
    position: absolute; left: 37px; top: 320px;
    font-family: 'Anton', sans-serif; font-weight: 400; font-size: 34px; line-height: 42px;
    color: var(--paper); letter-spacing: 1.4px;
  }
  .gold-rule { position: absolute; height: 5px; background: var(--gold); transform: skewX(-40deg); }
  .front-rule { left: 41px; top: 458px; width: 226px; }
  .front-body {
    position: absolute; left: 39px; top: 489px; width: 400px;
    font-family: 'Outfit', sans-serif; font-weight: 500; font-size: 15.4px; line-height: 23.6px;
    color: var(--paper); text-transform: uppercase; white-space: nowrap;
  }

  /* Back */
  .back-photo {
    position: absolute; left: 0; top: 0; width: 451px; height: 360px;
    background: linear-gradient(180deg, #0b0908 0%, #1c1511 40%, #0e0b09 60%, #050505 100%);
  }
  .back-headline {
    position: absolute; left: 10px; top: 70px; width: 220px; text-align: center;
    font-family: 'Bebas Neue', sans-serif; font-weight: 400; font-size: 33px; line-height: 33.5px;
    color: var(--paper);
  }
  .help-panel {
    position: absolute; left: 247px; top: 65px; width: 187px; height: 334px;
    background: var(--ink);
  }
  .help-title {
    position: absolute; left: 0; top: 40px; width: 187px; text-align: center;
    font-family: 'Anton', sans-serif; font-weight: 400; font-size: 22px; line-height: 27px;
    color: var(--paper); letter-spacing: 1px;
  }
  .help-rule { left: 45px; top: 105px; width: 98px; height: 3px; }
  .help-list { position: absolute; left: 18px; top: 128px; list-style: none; }
  .help-list li {
    position: relative; padding-left: 27px; white-space: nowrap;
    font-family: 'Outfit', sans-serif; font-weight: 600; font-size: 14px; line-height: 28px;
    color: var(--paper);
  }
  .help-list li::before {
    content: ""; position: absolute; left: 2px; top: 9px; width: 11px; height: 11px;
    border: 1.5px solid var(--paper);
  }
  .back-brand {
    position: absolute; left: 128px; top: 326px; width: 106px; text-align: center;
    font-family: 'Outfit', sans-serif; font-weight: 700; font-size: 15px; line-height: 18px;
    color: var(--ink); letter-spacing: 1px;
  }
  .contact-title {
    position: absolute; left: 17px; top: 427px;
    font-family: 'Anton', sans-serif; font-weight: 400; font-size: 18px; line-height: 24px; color: var(--ink);
    letter-spacing: 0.6px;
  }
  .contact-rule { left: -6px; top: 458px; width: 108px; }
  .contact-list { position: absolute; left: 17px; top: 474px; list-style: none; }
  .contact-list li {
    position: relative; padding-left: 25px;
    font-family: 'Outfit', sans-serif; font-weight: 600; font-size: 13px; line-height: 15.6px;
    color: var(--ink);
  }
  .contact-list li + li { margin-top: 6px; }
  .contact-list svg { position: absolute; left: 0; top: 1px; }
  .contact-list .phone {
    font-family: 'Anton', sans-serif; font-weight: 400; font-size: 23px; line-height: 30px;
    letter-spacing: 0.6px;
  }
  .contact-list .phone svg { top: 8px; }
  .stamp-box { position: absolute; left: 362px; top: 431px; width: 68px; height: 68px; border: 1px solid #333; }
  .address-line { position: absolute; left: 234px; width: 199px; height: 1px; background: #222; }
  .footer-band {
    position: absolute; left: 0; bottom: 0; width: 451px; height: 42px; background: var(--ink);
    display: flex; align-items: center; justify-content: center;
    font-family: 'Outfit', sans-serif; font-weight: 500; font-size: 10px; color: var(--paper);
    white-space: nowrap;
  }
</style>
</head>
<body>
<div class="canvas">

  <section class="card card--front">
    <div class="front-photo" role="img" aria-label="Photo placeholder: city skyline at sunset over a river"></div>
    <svg class="shapes" viewBox="0 0 806 1129" preserveAspectRatio="none" aria-hidden="true">
      <polygon points="478,0 806,0 806,168 645,203 478,168" fill="var(--mist)"/>
      <polygon points="0,373 806,612 806,628 0,390" fill="var(--paper)"/>
      <polygon points="0,390 806,628 806,1129 0,1129" fill="var(--ink)"/>
    </svg>
    <div class="brand-tag">HARBOR PATH<br>PARTNERS LLC</div>
    <h1 class="front-headline">FACING<br>FORECLOSURE?<br>YOU STILL HAVE OPTIONS.</h1>
    <div class="gold-rule front-rule"></div>
    <p class="front-body">If you’re behind on payments or at risk of<br>foreclosure, you’re not alone—and it’s<br>not too late to take action.</p>
  </section>

  <section class="card card--back">
    <div class="back-photo" role="img" aria-label="Photo placeholder: dark city skyline at dusk"></div>
    <svg class="shapes" viewBox="0 0 807 1129" preserveAspectRatio="none" aria-hidden="true">
      <polygon points="0,625 807,383 807,1129 0,1129" fill="var(--paper)"/>
    </svg>
    <h2 class="back-headline">No pressure.<br>No obligation.<br>Just real solutions<br>tailored to your<br>situation.</h2>

    <div class="help-panel">
      <h3 class="help-title">WE HELP<br>HOMEOWNERS</h3>
      <div class="gold-rule help-rule"></div>
      <ul class="help-list">
        <li>Explore options to<br>stay in their home</li>
        <li>Stop or delay<br>foreclosure</li>
        <li>Sell quickly for a<br>fair price if needed</li>
      </ul>
    </div>

    <div class="back-brand">HARBOR PATH PARTNERS</div>

    <h3 class="contact-title">CONTACT US</h3>
    <div class="gold-rule contact-rule"></div>
    <ul class="contact-list">
      <li>
        <svg width="14" height="18" viewBox="0 0 14 18" aria-hidden="true"><path d="M7 0a7 7 0 0 0-7 7c0 5 7 11 7 11s7-6 7-11a7 7 0 0 0-7-7z" fill="var(--gold)"/><circle cx="7" cy="7" r="2.6" fill="var(--paper)"/></svg>
        Harbor Path Partners LLC<br>7200 Bramwick Lane,<br>Ellicott City, MD 21043
      </li>
      <li>
        <svg width="15" height="12" viewBox="0 0 15 12" aria-hidden="true"><rect x="0.5" y="1.5" width="14" height="10" fill="var(--gold)"/><path d="M0.5 1.5l7 5.5 7-5.5" fill="none" stroke="var(--paper)" stroke-width="1.2"/></svg>
        marcus@hpbllc-mail.com
      </li>
      <li class="phone">
        <svg width="15" height="15" viewBox="0 0 24 24" aria-hidden="true"><path d="M6.6 10.8a15 15 0 0 0 6.6 6.6l2.2-2.2a1 1 0 0 1 1-.25 11.4 11.4 0 0 0 3.6.57 1 1 0 0 1 1 1V20a1 1 0 0 1-1 1A17 17 0 0 1 3 4a1 1 0 0 1 1-1h3.5a1 1 0 0 1 1 1c0 1.25.2 2.45.57 3.570a1 1 0 0 1-.25 1z" fill="none" stroke="var(--gold)" stroke-width="2"/></svg>
        (240) 558-2094
      </li>
    </ul>

    <div class="stamp-box"></div>
    <div class="address-line" style="top:520px"></div>
    <div class="address-line" style="top:545px"></div>
    <div class="address-line" style="top:570px"></div>

    <footer class="footer-band">Marcus Fennimore is a Licensed Realtor with Copperleaf Homes Realty in Bethesda, Maryland.</footer>
  </section>

</div>
</body>
</html>
```